Book Cover,

Our book is called "88 methods for wrecking your life but staying upright: Enduring Past University, Still one more Clichéd Diploma-era Coping Manual.
The Cover art for our book is very vivid in our minds and we hope YOU can help us bring it to life!

Picture a college graduation, cap, gown, cameras stadium the whole nine yards. now focus on one college graduate a guy, long black hair, diploma in his had, facing the crowd, his parents, flashes going off around him, behind him, is the exit of the graduation ceremony, where his class mates are exiting, but its not an exit, its the edge of a massive cliff, and students are falling down, you see people mid air falling down, at the bottom of the cliff is a trampoline, where the kids are bouncing off,

the idea and theory behind the art is the moral of the book, the book is a satire on all post college survival guides, (and god only knows how many horrible ones are out there). This is to make fun of them shed some light on the situation and really give good clear advice. so the art needs to be fun cartoonish feel and really scream satire.

Please dont hesitate to ask us for more direction, but we hope this is a great start!
Updates

Reason: We have not found something that we are set on please send us more submissions!

Reason: We have seen things we like but arent sold on any one yet- as well we have both been out of the country and have not had time to seriously consider all the submissions thank you

Target Market(s)

17-25

Industry/Entity Type

College

Requirements
Must have
• lots of colors, we want the art to be very vibrant, also a pencil look, we want the art to look like it was drawn onto the book
Should not have
• should not look digital it needs to have a real art feel to it.

```html
<!DOCTYPE html>
<html lang="en">
<head>
<meta charset="utf-8">
<title>88 Methods for Wrecking Your Life but Staying Upright – Book Cover</title>
<link rel="stylesheet" href="https://fonts.googleapis.com/css2?family=Bebas+Neue&family=Roboto+Condensed:wght@700&display=swap">
<style>
  :root {
    --stage: #9b9b9b;
    --paper: #ffffff;
    --band-orange: #f9a035;
    --band-red: #e8333a;
    --band-black: #000000;
    --ink: #111111;
    --ink-soft: #3a3a3a;
    --rule: #c9c9c9;
    --art-tone-light: #c8b8aa;
    --art-tone-deep: #9a7f6a;
  }
  html, body {
    margin: 0;
    padding: 0;
    width: 1200px;
    height: 1000px;
    overflow: hidden;
    background: var(--stage);
  }
  .book-cover {
    position: absolute;
    left: 353px;
    top: 105px;
    width: 494px;
    height: 790px;
    background: var(--paper);
    overflow: hidden;
  }
  .title-block {
    position: absolute;
    left: 0;
    top: 0;
    display: block;
  }
  .title-text {
    font-family: "Bebas Neue", "Oswald", sans-serif;
    fill: var(--paper);
  }
  .cover-art {
    position: absolute;
    left: 175px;
    top: 373px;
    width: 194px;
    height: 187px;
    background: linear-gradient(180deg, var(--art-tone-light), var(--art-tone-deep));
  }
  .subtitle {
    position: absolute;
    left: 0;
    top: 580px;
    display: block;
  }
  .subtitle-text {
    font-family: "Bebas Neue", "Oswald", sans-serif;
    fill: var(--ink);
  }
  .divider {
    position: absolute;
    left: 25px;
    top: 733px;
    width: 444px;
    height: 0;
    border-top: 1px solid var(--rule);
  }
  .author-name {
    position: absolute;
    left: 0;
    top: 742px;
    width: 494px;
    margin: 0;
    text-align: center;
    font-family: "Roboto Condensed", "Arial Narrow", sans-serif;
    font-weight: 700;
    font-size: 30px;
    line-height: 36px;
    letter-spacing: 5px;
    text-indent: 5px;
    color: var(--ink-soft);
  }
</style>
</head>
<body>
  <main class="book-cover">
    <svg class="title-block" width="494" height="331" viewBox="0 0 494 331" role="heading" aria-level="1"
         aria-label="88 methods for wrecking your life but staying upright">
      <rect class="band band-orange" x="0" y="0" width="494" height="148" fill="var(--band-orange)"/>
      <rect class="band band-red" x="0" y="148" width="494" height="85" fill="var(--band-red)"/>
      <rect class="band band-black" x="0" y="233" width="494" height="98" fill="var(--band-black)"/>
      <text class="title-text" x="27" y="138" font-size="175" textLength="440" lengthAdjust="spacingAndGlyphs">88 METHODS</text>
      <text class="title-text" x="29" y="225" font-size="97" textLength="436" lengthAdjust="spacingAndGlyphs">FOR WRECKING YOUR LIFE</text>
      <text class="title-text" x="27" y="317" font-size="108" textLength="440" lengthAdjust="spacingAndGlyphs">BUT STAYING UPRIGHT</text>
    </svg>

    <div class="cover-art" role="img" aria-label="Photograph: a green sprout growing out of an old rusted padlock"></div>

    <svg class="subtitle" width="494" height="130" viewBox="0 0 494 130" aria-label="Enduring Past University, Still one more Clichéd Diploma-era Coping Manual">
      <text class="subtitle-text" x="92" y="42" font-size="29" textLength="310" lengthAdjust="spacingAndGlyphs">ENDURING PAST UNIVERSITY,</text>
      <text class="subtitle-text" x="92" y="80" font-size="29" textLength="310" lengthAdjust="spacingAndGlyphs">STILL ONE MORE CLICHÉD</text>
      <text class="subtitle-text" x="92" y="118" font-size="29" textLength="310" lengthAdjust="spacingAndGlyphs">DIPLOMA-ERA COPING MANUAL</text>
    </svg>

    <div class="divider"></div>
    <p class="author-name">AUTHOR NAME</p>
  </main>
</body>
</html>
```